VLM8 Business Card Design Project

Design which catches the client with the first impression. A design which is professional and classy with elegance. We have also got another project running and the winning prize for that is $240 "vlm8 print + graphic design".
For all the company details please visit www.vlm8-example.com.
Please find the logo attached and i would like to have good colors for my business card.
, Design which catches the client with the first impression. A design which is professional and classy with elegance.
Updates
VLM8 is running two projects at the same time, please feel free to participate. The other project name is

```html
<!DOCTYPE html>
<html lang="en">
<head>
<meta charset="utf-8">
<title>VLM8 Business Cards</title>
<link rel="stylesheet" href="https://fonts.googleapis.com/css2?family=Roboto+Slab:wght@400;500&display=swap">
<style>
  :root {
    --backdrop: #b9bbbe;
    --card-black: #050505;
    --card-green: #9dcb3a;
    --accent-teal: #3dae8a;
    --ink: #111111;
    --social-chip: #6f8fb0;
  }
  * { margin: 0; padding: 0; box-sizing: border-box; }
  html, body { width: 1200px; height: 900px; overflow: hidden; }
  body {
    background: var(--backdrop);
    font-family: "Roboto Slab", Georgia, serif;
    position: relative;
  }
  .card {
    position: absolute;
    width: 420px;
    height: 240px;
    background: var(--card-green);
    overflow: hidden;
    color: var(--ink);
  }
  .card-wave { position: absolute; inset: 0; width: 420px; height: 240px; }
  .social-row { position: absolute; left: 53px; top: 38px; display: flex; gap: 5px; }
  .social-chip { width: 14px; height: 14px; border-radius: 2px; background: var(--social-chip); }
  .brand-name {
    position: absolute;
    left: 240px; top: 70px;
    font-size: 36px;
    font-weight: 500;
    color: var(--accent-teal);
    letter-spacing: 1px;
    line-height: 1;
  }
  .person { position: absolute; left: 30px; top: 142px; }
  .person-name { font-size: 12.5px; font-weight: 400; line-height: 1.2; white-space: nowrap; }
  .person-role { font-size: 8.5px; line-height: 1.3; white-space: nowrap; }
  .contact-list { list-style: none; position: absolute; left: 30px; top: 178px; }
  .contact-item { display: flex; align-items: center; gap: 5px; font-size: 8.5px; height: 15px; white-space: nowrap; }
  .contact-icon { width: 9px; height: 9px; flex: none; }
  .card--one { left: 170px; top: 62px; }
  .card--two { left: 617px; top: 62px; }
  .card--three { left: 170px; top: 333px; }
  .card--four { left: 617px; top: 333px; }
  .card--five { left: 170px; top: 601px; }
</style>
</head>
<body>

<svg width="0" height="0" style="position:absolute">
  <defs>
    <symbol id="wave" viewBox="0 0 420 240">
      <path d="M0 0H420V102C372 120 312 130 250 128C170 126 90 100 0 95Z" fill="#050505"/>
      <path d="M55 112C130 120 190 132 250 132C320 132 380 116 420 104L420 111C380 124 320 139 250 139C185 139 125 125 55 112Z" fill="#3dae8a"/>
    </symbol>
    <symbol id="icon-phone" viewBox="0 0 10 10">
      <rect x="2.5" y="0.5" width="5" height="9" rx="1" fill="none" stroke="#111" stroke-width="1"/>
      <rect x="4" y="7.3" width="2" height="0.9" fill="#111"/>
    </symbol>
    <symbol id="icon-mail" viewBox="0 0 10 10">
      <rect x="0.5" y="2" width="9" height="6" fill="#111"/>
      <path d="M0.5 2L5 5.5L9.5 2" fill="none" stroke="#9dcb3a" stroke-width="0.8"/>
    </symbol>
    <symbol id="icon-globe" viewBox="0 0 10 10">
      <circle cx="5" cy="5" r="4.3" fill="none" stroke="#111" stroke-width="0.9"/>
      <ellipse cx="5" cy="5" rx="1.8" ry="4.3" fill="none" stroke="#111" stroke-width="0.7"/>
      <path d="M0.7 5H9.3" stroke="#111" stroke-width="0.7"/>
    </symbol>
  </defs>
</svg>

<article class="card card--one">
  <svg class="card-wave"><use href="#wave"/></svg>
  <div class="social-row"><span class="social-chip"></span><span class="social-chip"></span><span class="social-chip"></span></div>
  <div class="brand-name">VLM8</div>
  <div class="person">
    <h2 class="person-name">Aravindan Kesavamurthy</h2>
    <p class="person-role">Manager - Lighting and Flooring Division</p>
  </div>
  <ul class="contact-list">
    <li class="contact-item"><svg class="contact-icon"><use href="#icon-phone"/></svg>(+61) 400 000 101</li>
    <li class="contact-item"><svg class="contact-icon"><use href="#icon-mail"/></svg>aravindan.kesavamurthy@vlm8-example.com</li>
    <li class="contact-item"><svg class="contact-icon"><use href="#icon-globe"/></svg>www.vlm8-example.com</li>
  </ul>
</article>

<article class="card card--two">
  <svg class="card-wave"><use href="#wave"/></svg>
  <div class="social-row"><span class="social-chip"></span><span class="social-chip"></span><span class="social-chip"></span></div>
  <div class="brand-name">VLM8</div>
  <div class="person">
    <h2 class="person-name">Nilavendhan Rajagopal</h2>
    <p class="person-role">Manager - Childcare Services</p>
  </div>
  <ul class="contact-list">
    <li class="contact-item"><svg class="contact-icon"><use href="#icon-phone"/></svg>(+61) 400 000 202</li>
    <li class="contact-item"><svg class="contact-icon"><use href="#icon-mail"/></svg>nilavendhan.rajagopal@vlm8-example.com</li>
    <li class="contact-item"><svg class="contact-icon"><use href="#icon-globe"/></svg>www.vlm8-example.com</li>
  </ul>
</article>

<article class="card card--three">
  <svg class="card-wave"><use href="#wave"/></svg>
  <div class="social-row"><span class="social-chip"></span><span class="social-chip"></span><span class="social-chip"></span></div>
  <div class="brand-name">VLM8</div>
  <div class="person">
    <h2 class="person-name">Madhavi Venkataraman</h2>
    <p class="person-role">Manager - Human Resources</p>
  </div>
  <ul class="contact-list">
    <li class="contact-item"><svg class="contact-icon"><use href="#icon-phone"/></svg>(+61) 400 000 303</li>
    <li class="contact-item"><svg class="contact-icon"><use href="#icon-mail"/></svg>madhavi.venkataraman@vlm8-example.com</li>
    <li class="contact-item"><svg class="contact-icon"><use href="#icon-globe"/></svg>www.vlm8-example.com</li>
  </ul>
</article>

<article class="card card--four">
  <svg class="card-wave"><use href="#wave"/></svg>
  <div class="social-row"><span class="social-chip"></span><span class="social-chip"></span><span class="social-chip"></span></div>
  <div class="brand-name">VLM8</div>
  <div class="person">
    <h2 class="person-name">Kavya Iyer</h2>
    <p class="person-role">Director</p>
  </div>
  <ul class="contact-list">
    <li class="contact-item"><svg class="contact-icon"><use href="#icon-phone"/></svg>(+61) 400 000 404</li>
    <li class="contact-item"><svg class="contact-icon"><use href="#icon-mail"/></svg>kavya.iyer@vlm8-example.com</li>
    <li class="contact-item"><svg class="contact-icon"><use href="#icon-globe"/></svg>www.vlm8-example.com</li>
  </ul>
</article>

<article class="card card--five">
  <svg class="card-wave"><use href="#wave"/></svg>
  <div class="social-row"><span class="social-chip"></span><span class="social-chip"></span><span class="social-chip"></span></div>
  <div class="brand-name">VLM8</div>
  <div class="person">
    <h2 class="person-name">Suresh Balakrishnan</h2>
    <p class="person-role">Director</p>
  </div>
  <ul class="contact-list">
    <li class="contact-item"><svg class="contact-icon"><use href="#icon-phone"/></svg>(+61) 400 000 505</li>
    <li class="contact-item"><svg class="contact-icon"><use href="#icon-mail"/></svg>suresh.balakrishnan@vlm8-example.com</li>
    <li class="contact-item"><svg class="contact-icon"><use href="#icon-globe"/></svg>www.vlm8-example.com</li>
  </ul>
</article>

</body>
</html>
```